National Brochure Design Project

We are looking for a brochure design which will be used for a National retailer within the plumbing home improvement market.
The brochure is used to promote products which are available to order in, therefore the key theme of the brochure is 'inspiration'. Our order in range is typically higher end product so we are looking for a clean, modern layout that will showcase our extended product ranges.

The industry in which we play has a vast range of products which we can order in, therefore the layout needs to be flexible to allow for pages where multiple small products can be displayed and pages where only few larger products can be displayed as image sizes will vary.

The main message this brochure should communicate is more choice through using inspirational images and a modern design which will showcase our top end order in products.

Target Market(s)

Our target market is the household female who shops based on inspiration and feelings rather than just product information.

Industry/Entity Type

Home Improvement

Requirements
Must have
• The brochure must be an A4 landscape design (210h x 260w mm).
At the bottom of each page there must be a footer 20mm high across the entire page width, this must appear on all pages and must be orange. Orange is the corporate colour and can be used where appropriate in the design.

Font used should be Arial for the main copy within the brochure, cover/title/subheading font can differ but must still be esily legible.

On the front cover, the brochure title/heading must appear in the top 1/3rd of the page and a rectangle logo (White, 50h x 32w mm - or to scale of this size) needs to be included into this same space.

The design must include the following pages:
- A front cover (Inspirational image/s with talent is preferred) (Page 1)
- Contents and ordering information page (Page 2) (Image/s can be used if within the design concept)
- (Page 3) This is the first page which introduces the brochure, this can either be a design page with inspirational image/s, or can be an information page or it could be the first product page. This page is part of the spread you will see when you first open the brochure and should entice the customer to want to turn the page to see what else is on offer.
- A spread (Pages 4 and 5) with the LHS page being a full colour insitu inspirational image/s and the RHS page being product information (studio shots) etc. with product names and information.
- A spread (Pages 6 and 7) where there is no full page insitu images used, however both pages are to showcase products and provide the customer with information on sizes, colour options, features and benefits etc.

Any additional pages/designs are welcome to review but a minimum of the above 7 pages are required.
Nice to have
• Full page insitu images on the left hand side page of a spread. This won't be used on all spreads but the aim is to include more insitu inspirational images. Anyway in which these kind of images can be incorporated if not full page are welcomed for review.

Where possible we may reference the insitu image (a,b,c) and list the product details on following product information pages, otherwise the insitu will just be used to give the audience an idea of what you can create and the product information will be included on following pages with studio shots of each item.

An idea is to include callouts on some pages referring customers to the website to look at pricing and further ranges, any ideas welcomed of ways this message can be included inline with a design concept.

We have not supplied any product information or images which are to be used, we are happy to have any images you feel work within your design included and copy doesn't need to be specific but can be repeated generic text.
Should not have
• Please do not include illustrations or cartoon like images, the look and feel should be clean and modern.

```html
<!DOCTYPE html>
<html lang="en">
<head>
<meta charset="utf-8">
<title>Brochure – Page 2: Contents and Ordering Information</title>
<link rel="stylesheet" href="https://fonts.googleapis.com/css2?family=Cinzel:wght@400&family=Arimo:wght@400;700&display=swap">
<style>
  :root {
    --lime: #d3dc3e;
    --olive: #b6bb35;
    --olive-dark: #8e9431;
    --white: #ffffff;
    --orange: #f1592a;
    --amber: #f0a52f;
    --amber-light: #f5b93a;
    --photo-teal: #7d9aa3;
    --photo-stone: #c9ccc4;
    --photo-stripe: #e7a23a;
    --photo-wood: #6b3b2a;
  }
  * { margin: 0; padding: 0; box-sizing: border-box; }
  html, body { width: 1200px; height: 848px; overflow: hidden; }
  body { background: var(--lime); font-family: "Arimo", Arial, sans-serif; }

  .page { position: relative; width: 1200px; height: 848px; background: var(--lime); overflow: hidden; }

  .trim-frame {
    position: absolute; left: 81px; top: 81px; width: 1035px; height: 607px;
    border: 1px solid var(--white);
  }

  .contents-panel {
    position: absolute; left: 148px; top: 131px; width: 360px; height: 270px;
    background: var(--olive);
  }
  .panel-tab { position: absolute; background: var(--olive-dark); }
  .contents-panel .panel-tab { left: 0; top: 0; width: 38px; height: 94px; }

  .section-title {
    position: absolute; font-family: "Cinzel", "Times New Roman", serif;
    font-weight: 400; color: var(--white); line-height: 1; letter-spacing: 1px;
  }
  .contents-panel .section-title { left: 41px; top: 32px; font-size: 50px; }

  .contents-list { position: absolute; left: 41px; top: 105px; width: 286px; list-style: none; }
  .contents-list li {
    display: flex; align-items: baseline; color: var(--white);
    font-size: 11px; height: 26.8px;
  }
  .contents-list .page-no { flex: 0 0 auto; }
  .contents-list .leader {
    flex: 1 1 auto; overflow: hidden; white-space: nowrap; letter-spacing: 2px;
  }
  .contents-list .leader::before { content: ". . . . . . . . . . . . . . . . . . . . . . . . . . . . . . . . . . . . . ."; letter-spacing: 0; }
  .contents-list .topic { flex: 0 0 auto; }

  .photo { position: absolute; }
  .photo-wash {
    left: 148px; top: 403px; width: 360px; height: 239px;
    background: linear-gradient(180deg, var(--photo-teal) 0%, #9fb2b5 45%, var(--photo-stone) 75%, #eef0ec 100%);
  }
  .photo-vanity {
    left: 690px; top: 81px; width: 361px; height: 283px;
    background: linear-gradient(160deg, var(--photo-stripe) 0%, #c9cf49 35%, #f3efe6 60%, var(--photo-wood) 100%);
  }

  .ordering-panel {
    position: absolute; left: 690px; top: 364px; width: 361px; height: 322px;
    background: var(--olive);
  }
  .ordering-panel .panel-tab { left: 0; top: 35px; width: 40px; height: 81px; }
  .ordering-panel .section-title { left: 49px; top: 47px; font-size: 55px; }
  .section-subtitle {
    position: absolute; left: 51px; top: 95px;
    font-family: "Cinzel", "Times New Roman", serif; font-size: 13px;
    color: var(--white); letter-spacing: 14.2px; line-height: 1;
  }
  .ordering-copy { position: absolute; left: 49px; top: 133px; width: 305px; }
  .ordering-copy p {
    color: var(--white); font-size: 11px; line-height: 1.36; margin-bottom: 13px;
  }

  .footer-band { position: absolute; left: 0; top: 766px; width: 1200px; height: 82px; }
  .footer-rule { position: absolute; left: 1116px; top: 780px; width: 1px; height: 68px; background: var(--white); }
  .page-number {
    position: absolute; left: 1121px; top: 809px;
    font-size: 11px; color: var(--white);
  }
</style>
</head>
<body>
<main class="page">
  <div class="trim-frame"></div>

  <section class="contents-panel">
    <div class="panel-tab"></div>
    <h1 class="section-title">CONTENTS</h1>
    <ol class="contents-list">
      <li><span class="page-no">3</span><span class="leader"></span><span class="topic">Topic of having a great</span></li>
      <li><span class="page-no">4</span><span class="leader"></span><span class="topic">Topic of having a great</span></li>
      <li><span class="page-no">5</span><span class="leader"></span><span class="topic">Topic of having a great</span></li>
      <li><span class="page-no">6</span><span class="leader"></span><span class="topic">Topic of having a great</span></li>
      <li><span class="page-no">7</span><span class="leader"></span><span class="topic">Topic of having a great</span></li>
    </ol>
  </section>

  <div class="photo photo-wash" role="img" aria-label="Photo of a woman rinsing her face at a modern bathroom basin in front of a large mirror"></div>
  <div class="photo photo-vanity" role="img" aria-label="Photo of a bathroom vanity with a white vessel basin on a dark wood top, wood-framed mirror and bold horizontal wall stripes"></div>

  <section class="ordering-panel">
    <div class="panel-tab"></div>
    <h2 class="section-title">ORDERING</h2>
    <div class="section-subtitle">INFORMATIONS</div>
    <div class="ordering-copy">
      <p>All item on this brochure is available through on-line or via mail. Delivery will be 2 to 3 day after the submitted order form.</p>
      <p>Please log-in at www.homeverde-example.com to fill the form then wait for our confirmation before business transaction.</p>
      <p>All items were paased thru Quality Control to assure you the finest quality among the rest brands.</p>
      <p>Please call our 24/7 customer care hotline:&nbsp; 555-0142</p>
    </div>
  </section>

  <svg class="footer-band" viewBox="0 0 1200 82" preserveAspectRatio="none" aria-hidden="true">
    <rect x="0" y="0" width="1200" height="82" fill="var(--orange)"/>
    <polygon points="248,14 376,0 290,82 155,82" fill="var(--amber)"/>
    <polygon points="250,12 370,12 360,22 240,22" fill="var(--amber-light)"/>
    <polygon points="0,14 236,14 230,20 0,20" fill="#e8702b" opacity="0.6"/>
  </svg>
  <div class="footer-rule"></div>
  <div class="page-number">2</div>
</main>
</body>
</html>
```